I need 8 Banners for my Web Site

I am building an online store with prestashop, The store will sell costa rican coffee bags, I have the site almost ready, but I need some nice banners.

Top Banners
3 Banners
940x446

2 Banner
218x158

Footer Banners
3 Banners
280x100

Please see the attached images to see how they will fit in the web page.
Also you can see some of the products and images over here https://www.alderroastcrate.example/TheAlderRoastCrate

All I need is that the banners fit with the website design, and that they look "coffee related",(think about a coffee shop with fine coffee products, fresh coffee from a latin american country, think about a mountain full of coffee plants, think about nature, think about flavor)

Colors are brown,green, gray, white, but if you see something else can match those colors feel free to use them.

Also Below the texts you must Use:

3 Banners
940x446

#1
Welcome Coffee Lovers!
The Alder Roast Crate Store is Open Now!

#2
Fresh Coffee from the Costa Rican Mountains!
Get your coffee Now!

#3
Free Coffee Samples!
Fill our form and participate for weekly promotions!

2 Banners
218x158

#1
Carbon Neutral Coffee
Get it Now!

#2
Coffee from the TarrazĂș Mountains
Buy Now!

3 Banners
280x100

#1
Coffee from Veluna Ridge Farm
Shop Now!

#2
Moravo Roast, the finest beans to your door!
Shop Now!

#3
Check our Espresso catalog!
Shop Now!

```html
<!DOCTYPE html>
<html lang="en">
<head>
<meta charset="utf-8">
<title>Welcome Coffee Lovers – The Alder Roast Crate</title>
<link rel="stylesheet" href="https://fonts.googleapis.com/css2?family=Lobster&family=Montserrat:wght@300;400;700;800&display=swap">
<style>
  :root {
    --parchment-light: #f1dfb8;
    --parchment-mid: #e2c592;
    --parchment-edge: #b98d55;
    --ink: #2a2421;
    --leaf-green: #1d7a3a;
    --bean-dark: #2e1a10;
    --bean-mid: #6b3f22;
    --cup-black: #141110;
    --cup-cream: #efe6da;
    --crema: #5a3520;
  }
  * { margin: 0; padding: 0; box-sizing: border-box; }
  html, body { width: 1200px; height: 569px; overflow: hidden; background: #ffffff; }

  .banner {
    position: relative;
    width: 1200px;
    height: 569px;
    overflow: hidden;
    background:
      radial-gradient(ellipse 60% 70% at 42% 38%, var(--parchment-light) 0%, var(--parchment-mid) 55%, var(--parchment-edge) 100%);
    font-family: "Montserrat", Arial, sans-serif;
    color: var(--ink);
  }

  .beans-photo {
    position: absolute;
    left: 0; top: 0;
    width: 230px; height: 569px;
    background:
      linear-gradient(90deg, var(--bean-dark) 0%, var(--bean-mid) 45%, rgba(107,63,34,0.55) 75%, rgba(107,63,34,0) 100%);
  }

  .cup-illustration {
    position: absolute;
    left: 750px; top: 0;
    width: 450px; height: 569px;
    background:
      radial-gradient(circle 232px at 233px 243px, var(--crema) 0%, var(--crema) 38%, var(--cup-cream) 40%, var(--cup-cream) 62%, var(--cup-black) 64%, var(--cup-black) 99%, rgba(20,17,16,0) 100%),
      linear-gradient(90deg, rgba(120,80,40,0) 0%, #6e4a28 40%, #3a2616 100%);
  }

  .headline-block {
    position: absolute;
    left: 289px; top: 0;
    width: 400px;
    text-align: center;
  }

  .welcome {
    position: absolute;
    left: 0; right: 0; top: 30px;
    font-family: "Lobster", "Brush Script MT", cursive;
    font-size: 36px;
    color: var(--leaf-green);
    line-height: 1;
  }

  .title {
    position: absolute;
    left: 0; right: 0; top: 96px;
    font-size: 84px;
    line-height: 72px;
    letter-spacing: 1px;
    text-transform: uppercase;
  }
  .title .strong { display: block; font-weight: 800; }
  .title .light { display: block; font-weight: 300; margin-top: 0; }

  .store-name {
    position: absolute;
    left: 0; right: 0; top: 318px;
    display: flex;
    align-items: center;
    justify-content: center;
    gap: 12px;
  }
  .store-name .dot {
    width: 46px; height: 46px;
    border-radius: 50%;
    background: var(--leaf-green);
  }
  .store-name .name {
    font-weight: 700;
    font-size: 26px;
    color: var(--leaf-green);
    line-height: 1.1;
    text-align: left;
  }

  .tagline {
    position: absolute;
    left: 0; right: 0; top: 441px;
    font-weight: 700;
    font-size: 18px;
    color: var(--leaf-green);
  }

  .open-now {
    position: absolute;
    left: 0; right: 0; top: 484px;
    font-weight: 800;
    font-size: 46px;
    letter-spacing: 1px;
    text-transform: uppercase;
  }
</style>
</head>
<body>
  <main class="banner">
    <div class="beans-photo" role="img" aria-label="Roasted coffee beans scattered along the left edge"></div>
    <div class="cup-illustration" role="img" aria-label="Top view of a black coffee cup on a saucer with the words Open Now in the coffee, over brown stripes"></div>

    <section class="headline-block">
      <p class="welcome">Welcome</p>
      <h1 class="title"><span class="strong">Coffee</span><span class="light">Lovers!</span></h1>
      <div class="store-name">
        <span class="dot"></span>
        <span class="name">The Alder Roast<br>Crate</span>
      </div>
      <p class="tagline">Costa Rican Coffee Online</p>
      <p class="open-now">Open Now!</p>
    </section>
  </main>
</body>
</html>
```